Alapca breeding needs a website

Presentation of the farm, animals (stallions, mares, information about the animals, for sale) and possible later expansion with a webshop (alpaca wool products). We want to present our farm and the animals on the farm on this page. A mission why we are doing this. Furthermore, each animal should be shown with a picture and described. Later we want to sell our own products made from alpaca wool via a webshop. But we still need to grow a bit to do that.

Target Market(s)

Information about my alpaca breeding and the alpaca farm

Industry/Entity Type

Tierzucht

Number of Pages Required

1 page

Font styles to use
Sans Serif

Requirements
Must have
• Modern design that matches the logo
Nice to have
• Intuitive operation / Clear structure
Should not have
• No

```html
<!DOCTYPE html>
<html lang="en">
<head>
<meta charset="utf-8">
<title>Meadowlane Alpacas</title>
<link href="https://fonts.googleapis.com/css2?family=Cinzel:wght@600;700&family=Raleway:wght@500;600;700&display=swap" rel="stylesheet">
<style>
:root{
  --navy:#0b2340;
  --green:#8dc63f;
  --green-soft:#e9f3db;
  --white:#ffffff;
  --ink:#1d1d1d;
  --line:#b9b9b9;
}
*{margin:0;padding:0;box-sizing:border-box}
html,body{width:1200px;height:4217px;overflow:hidden}
body{position:relative;background:var(--white);font-family:"Raleway",Arial,sans-serif;color:var(--ink)}
.abs{position:absolute}
.serif{font-family:"Cinzel",Georgia,serif;font-weight:700}
.hl{color:var(--green)}
.btn{position:absolute;background:var(--green);color:var(--white);font-weight:600;display:flex;align-items:center;justify-content:center;border-radius:4px;letter-spacing:.5px}
.ph{position:absolute}
/* header */
.brand{left:111px;top:60px;width:200px;text-align:center;font-family:"Cinzel",serif;font-weight:700;color:var(--navy);font-size:30px;line-height:34px}
.brand-dot{position:absolute;left:170px;top:8px;width:46px;height:46px;border-radius:50%;background:var(--navy)}
.contact{display:flex;align-items:center;gap:18px}
.contact .ico{width:34px;height:34px;border-radius:50%;background:var(--green);display:flex;align-items:center;justify-content:center}
.contact .lab{color:var(--green);font-size:17px;font-weight:600}
.contact .val{font-size:16px;margin-top:14px}
.nav{left:315px;top:124px;width:885px;height:68px;background:var(--navy);clip-path:polygon(40px 0,100% 0,100% 100%,0 100%)}
.nav ul{list-style:none;display:flex;position:absolute;left:51px;top:24px;gap:0;font-size:16px;font-weight:600;color:var(--white)}
.nav li{margin-right:54px}
.nav li.on{color:var(--green)}
/* hero */
.hero{left:0;top:192px;width:1200px;height:594px;background:linear-gradient(180deg,#c9d9e4 0%,#d9d8b9 35%,#a9b85a 60%,#7d9a2e 100%)}
.hero h1{right:85px;top:350px;font-size:35px;color:var(--navy);letter-spacing:.5px}
.hero-copy{right:85px;top:420px;width:520px;text-align:right;font-size:17px;line-height:35px}
/* sections */
.h2{position:absolute;font-size:34px;color:var(--navy);letter-spacing:.5px}
.body{font-size:17px;line-height:35px}
.card{position:absolute;top:1475px;width:316px;height:489px;background:var(--white);border:2px solid #ddd;border-radius:4px;box-shadow:0 2px 6px rgba(0,0,0,.12);text-align:center}
.card.dark{background:var(--navy);border-color:var(--navy);color:var(--white)}
.card .ph{left:8px;top:8px;width:298px;height:224px}
.card h3{position:absolute;top:258px;width:100%;color:var(--green);font-size:23px;font-weight:600;letter-spacing:.5px}
.card p{position:absolute;top:300px;left:12px;right:12px;font-size:17px;line-height:36px}
.card .btn{left:85px;top:422px;width:144px;height:41px;font-size:15px}
.arrow{position:absolute;width:40px;height:40px;border-radius:50%;display:flex;align-items:center;justify-content:center}
.date{position:absolute;background:var(--navy);color:var(--white);font-size:20px;font-weight:600;text-align:center;line-height:38px;border-radius:4px}
.news-txt{position:absolute;left:751px;width:340px;font-size:17px;line-height:35px}
.rule{position:absolute;left:625px;width:455px;height:1px;background:var(--line)}
.flink{position:absolute;color:var(--white);font-size:16px;font-weight:700;letter-spacing:.3px;white-space:pre}
.soc{width:28px;height:28px;border:1.5px solid var(--white);border-radius:50%}
</style>
</head>
<body>

<!-- header -->
<div class="abs brand-dot" aria-hidden="true"></div>
<div class="abs brand">MEADOWLANE<br>ALPACAS</div>

<div class="abs contact" style="left:440px;top:30px">
  <div class="ico"><svg width="18" height="18" viewBox="0 0 24 24"><path fill="#fff" d="M6.6 10.8a15 15 0 0 0 6.6 6.6l2.2-2.2a1 1 0 0 1 1-.25 11.4 11.4 0 0 0 3.6.6 1 1 0 0 1 1 1V20a1 1 0 0 1-1 1A17 17 0 0 1 3 4a1 1 0 0 1 1-1h3.5a1 1 0 0 1 1 1c0 1.25.2 2.45.6 3.6a1 1 0 0 1-.25 1z"/></svg></div>
  <div><div class="lab">CALL US NOW</div><div class="val">+1 555 010 2020</div></div>
</div>
<div class="abs contact" style="left:734px;top:30px">
  <div class="ico"><svg width="18" height="18" viewBox="0 0 24 24" fill="none" stroke="#fff" stroke-width="2"><rect x="3" y="5" width="18" height="14" rx="2"/><path d="M3 7l9 6 9-6"/></svg></div>
  <div><div class="lab">MAIL US</div><div class="val">INFO@MEADOWLANEALPACA.EXAMPLE</div></div>
</div>
<div class="abs" style="left:1085px;top:45px;width:38px;height:38px;border-radius:50%;background:var(--green);display:flex;align-items:center;justify-content:center">
  <svg width="20" height="20" viewBox="0 0 24 24" fill="none" stroke="#fff" stroke-width="2"><path d="M2 3h3l2.5 12h11l2-8H6"/><circle cx="9" cy="20" r="1.5"/><circle cx="17" cy="20" r="1.5"/></svg>
</div>

<nav class="abs nav"><ul>
  <li class="on">HOME</li><li>OUR MISSION</li><li>OUR PRODUCTS</li><li>OUR FARM ANIMAL</li><li style="margin:0">CONTACT US</li>
</ul></nav>

<!-- hero -->
<section class="ph hero" role="img" aria-label="Chestnut horse standing in a sunny green meadow"></section>
<svg class="abs" style="left:0;top:700px" width="1200" height="90" viewBox="0 0 1200 90" aria-hidden="true"><path d="M0 10 Q600 170 1200 5 L1200 90 L0 90Z" fill="#fff"/></svg>
<h1 class="abs serif hero-h1" style="right:85px;top:350px;font-size:35px;color:var(--navy)">WELCOME TO MEADOWLANE ALPACAS</h1>
<p class="abs hero-copy">Lorem ipsum dolor sit amet, consectetur adipiscing elit, sed do eiusmod tempor incididunt ut labore et dolore magna aliqua.</p>
<div class="btn" style="left:933px;top:557px;width:182px;height:60px;font-size:22px">GET STARTED</div>

<!-- mission -->
<h2 class="h2 serif" style="left:110px;top:872px">OUR <span class="hl">MISSION</span></h2>
<p class="abs body" style="left:111px;top:945px;width:460px">Lorem ipsum dolor sit amet, consectetur adipiscing elit, sed do eiusmod tempor incididunt ut labore et dolore magna aliqua.  Ut enim ad minim veniam, quis nostrud exercitation ullamco laboris nisi ut aliquip ex ea commodo consequat. Duis aute irure dolor in reprehenderit in voluptate velit esse cillum dolore eu fugiat nulla pariatur.</p>
<div class="btn" style="left:111px;top:1221px;width:182px;height:59px;font-size:22px">LEARN MORE</div>
<div class="ph" role="img" aria-label="Two young lambs in a green field" style="left:620px;top:886px;width:396px;height:396px;border-radius:50%;background:radial-gradient(circle at 50% 30%,#c9c3a5,#8aa44a 60%,#5f7d2a)"></div>
<div class="ph" role="img" aria-label="Cows grazing in a pasture at sunset" style="left:863px;top:889px;width:228px;height:228px;border-radius:50%;border:5px solid #fff;background:radial-gradient(circle at 40% 40%,#f2d59a,#9fb46a 60%,#5d7a34)"></div>

<!-- products -->
<h2 class="h2 serif" style="left:0;width:1200px;text-align:center;top:1365px">ALPACAS WOOL <span class="hl">PRODUCTS</span></h2>
<div class="abs" style="left:0;top:1719px;width:1200px;height:352px;background:var(--green-soft)"></div>
<div class="arrow" style="left:27px;top:1699px;background:var(--navy)"><svg width="14" height="14" viewBox="0 0 24 24" fill="none" stroke="#fff" stroke-width="3"><path d="M15 4l-8 8 8 8"/></svg></div>
<div class="arrow" style="left:1123px;top:1699px;background:var(--green)"><svg width="14" height="14" viewBox="0 0 24 24" fill="none" stroke="#fff" stroke-width="3"><path d="M9 4l8 8-8 8"/></svg></div>

<div class="card" style="left:111px">
  <div class="ph" role="img" aria-label="Skeins of natural white alpaca yarn" style="background:linear-gradient(135deg,#e8e3d8,#bdb3a3 60%,#6b4a34)"></div>
  <h3>LOREM IPSUM</h3><p>Lorem ipsum dolor sit amet, consectetur adipiscing elit, sed do eiusmod tempor.</p>
  <div class="btn">ADD TO CART</div>
</div>
<div class="card dark" style="left:442px">
  <div class="ph" role="img" aria-label="Stacks of colourful woven alpaca blankets" style="background:linear-gradient(180deg,#6a3b2a,#c2473d 30%,#2f8d8b 55%,#d7a23a 80%,#b03a6a)"></div>
  <h3>LOREM IPSUM</h3><p>Lorem ipsum dolor sit amet, consectetur adipiscing elit, sed do eiusmod tempor.</p>
  <div class="btn">ADD TO CART</div>
</div>
<div class="card" style="left:771px">
  <div class="ph" role="img" aria-label="Balls of dyed alpaca wool in red and yellow" style="background:radial-gradient(circle at 50% 65%,#e2b53b,#8c1c2a 45%,#3d1120)"></div>
  <h3>LOREM IPSUM</h3><p>Lorem ipsum dolor sit amet, consectetur adipiscing elit, sed do eiusmod tempor.</p>
  <div class="btn">ADD TO CART</div>
</div>

<!-- animals for sale -->
<section class="abs" style="left:0;top:2072px;width:1200px;height:536px;background:var(--navy)"></section>
<div class="ph" role="img" aria-label="Woman with a dark horse in a golden sunlit field" style="left:0;top:2072px;width:606px;height:536px;clip-path:polygon(0 0,606px 0,504px 100%,0 100%);background:linear-gradient(135deg,#5d4a1c,#c8962f 45%,#7a6a24 75%,#3b3a14)"></div>
<h2 class="h2 serif" style="left:671px;top:2114px;color:#fff">ANIMALS FOR <span class="hl">SALE</span></h2>
<h3 class="abs serif hl" style="left:670px;top:2190px;font-size:28px">STALLIONS</h3>
<p class="abs body" style="left:671px;top:2245px;width:460px;color:#fff">Lorem ipsum dolor sit amet, consectetur adipiscing elit, sed do eiusmod tempor incididunt ut labore et dolore magna aliqua.  Ut enim ad minim veniam, quis nostrud exercitation ullamco laboris nisi ut aliquip ex ea commodo consequat.</p>
<div class="btn" style="left:671px;top:2456px;width:167px;height:54px;font-size:21px">VIEW DETAILS</div>
<div class="btn" style="left:849px;top:2456px;width:166px;height:54px;font-size:21px">ADD TO CART</div>
<svg class="abs" style="left:668px;top:2547px" width="70" height="24" viewBox="0 0 70 24" fill="none" stroke="#fff" stroke-width="2.5" aria-hidden="true"><path d="M12 3l-8 9 8 9M58 3l8 9-8 9"/></svg>

<!-- news -->
<h2 class="h2 serif" style="left:0;width:1200px;text-align:center;top:2694px">MEADOWLANE ALPACAS <span class="hl">NEWS</span></h2>
<div class="ph" role="img" aria-label="Rider on a brown horse during a dressage event" style="left:111px;top:2819px;width:488px;height:488px;border-radius:8px;background:linear-gradient(160deg,#5b6f8a,#8b4a26 40%,#5a2d17 70%,#1d2a3a)"></div>
<div class="date" style="left:111px;top:2819px;width:94px;height:123px;padding-top:22px;border-radius:8px 0 4px 0">FEB 23<br>2024</div>
<p class="abs" style="left:170px;top:3178px;width:370px;text-align:center;color:#fff;font-size:17px;line-height:35px">Lorem ipsum dolor sit amet, consectetur adipiscing elit, sed do eiusmod tempor incididunt ut labore.</p>

<div class="date" style="left:625px;top:2839px;width:92px;height:122px;padding-top:23px">JAN 23<br>2024</div>
<p class="news-txt" style="top:2847px">Lorem ipsum dolor sit amet, consectetur adipiscing elit, sed do eiusmod tempor incididunt ut labore.</p>
<div class="rule" style="top:2981px"></div>
<div class="date" style="left:625px;top:3006px;width:92px;height:122px;padding-top:23px">APR 06<br>2024</div>
<p class="news-txt" style="top:3012px">Lorem ipsum dolor sit amet, consectetur adipiscing elit, sed do eiusmod tempor incididunt ut labore.</p>
<div class="rule" style="top:3145px"></div>
<div class="date" style="left:625px;top:3168px;width:92px;height:122px;padding-top:23px">MAY 06<br>2024</div>
<p class="news-txt" style="top:3175px">Lorem ipsum dolor sit amet, consectetur adipiscing elit, sed do eiusmod tempor incididunt ut labore.</p>

<div class="btn" style="left:480px;top:3369px;width:240px;height:58px;font-size:22px">VIEW MORE NEWS</div>

<!-- newsletter -->
<section class="abs" style="left:0;top:3523px;width:1200px;height:694px;background:var(--navy)"></section>
<h2 class="h2 serif" style="left:0;width:1200px;text-align:center;top:3598px;color:#fff">SUBSCRIBE FOR OUR <span class="hl">NEWSLETTER</span></h2>
<div class="abs" style="left:363px;top:3693px;width:472px;height:57px;border:1.5px solid #fff;border-radius:5px"></div>
<div class="abs" style="left:378px;top:3711px;color:#fff;font-size:17px;font-weight:500">ENTER EMAIL ADDRESS</div>
<div class="btn" style="left:658px;top:3698px;width:172px;height:47px;font-size:22px">SUBSCRIBE</div>

<!-- footer -->
<svg class="abs" style="left:0;top:3820px" width="1200" height="397" viewBox="0 0 1200 397" aria-hidden="true"><path d="M0 85 Q600 -75 1200 85 L1200 397 L0 397Z" fill="#8dc63f"/></svg>
<div class="abs" style="left:235px;top:3925px;width:56px;height:56px;border-radius:50%;background:var(--navy)"></div>
<div class="abs" style="left:130px;top:4020px;width:270px;text-align:center;font-family:'Cinzel',serif;font-weight:700;color:var(--navy);font-size:38px;line-height:44px">MEADOWLANE<br>ALPACAS</div>

<div class="flink" style="left:624px;top:3953px">HOME       |       OUR MISSION       |       OUR PRODUCTS</div>
<div class="flink" style="left:727px;top:3994px">OUR FARM ANIMAL       |       CONTACT US</div>
<div class="flink" style="left:698px;top:4048px;font-size:14px">@2024 COPYRIGHTS     |     ALL RIGHTS RESERVED</div>
<div class="abs" style="left:891px;top:4098px;display:flex;gap:7px">
  <div class="soc"></div><div class="soc"></div><div class="soc"></div><div class="soc"></div><div class="soc"></div>
</div>

</body>
</html>
```